Creative UI design for web application

I need a new UI design for my web application. It will be used by small and micro business owners to plan & implement growth tactics.

I've attached the current design (which I'm open to be changed) - but in particular I need to design the centre of the screen, where the work actually happens.

There needs to be place for a title (YOUR BUSINESS) and description (say 1-2 paragraphs of text) - and am happy to include icons or imagery where makes sense. It may make sense for the user to be able to upload their business logo and name, for example.

This screen will be used by the business owner to understand the real value they offer potential customers and their point of difference - why they exist and why potential customers should care.

They'll use the information they put into this screen to plan things like their messaging.

Following that, there needs to be 2 sections in the dashboard.

The first section is titled "WHO YOU ARE"

The first section will include a number of boxes that the user can input information into, as follows:

- Logo
- Business name
- Business tag line
- Business vision
- Business bio
- Brand colours (these should end up as swatches based on the colour code they enter) - the colour code for each colour swatch should also be visible.
- Key competitors
- SWOT analysis (boxes to enter their strengths, weaknesses, opportunities and threats).

The second section is titled "WHY YOU EXIST"

The second section will include a number of boxes that the user can input information (text) into, as follows:

- Who are your ideal customers?
- What problem are you trying to solve for them?
- What pain points will this remove for them?
- How do you solve it?
- How else could this problem be solved?
- Who offers these other solutions?
- Why is your solution better?
- How much does your solution cost?
- What value are you providing to justify this cost?
- How will this make their life/job easier/better?

They should be able to write a decent amount of information in the boxes.

There should ideally be a place for a description for each of these text fields (for both section 1 & 2) as well so I can give them a little bit more direction around what to put in the box. Alternatively there could be a little icon (say a question mark or "i") that they could click on to view instructions. The instructions will be around 2-4 sentences long for each text field.

You have 2 options:

a) This all needs to appear on the one screen, and the navigation needs to be visible (as per the example attached but feel free to recreate this navigation)

Note: the page can scroll below the fold - but please provide the design for the full length of the page.

b) Potentially the 2 sections could actually be in 2 different items in the menu - YOUR BUSINESS and YOUR VALUE (which would sit next to YOUR BUSINESS and before YOUR CUSTOMER in the screenshot provided). feel free to design them as 2 separate screens if you prefer.

I have attached a screenshot of the app as it stands today (screen shot 2017) which would still exist in the new design but under a different section (the learn section from the plan2 mockup attached)

I have mocked up how this new screen could look if broken into 2 and that's also attached. If you can make this come to life - and look more engaging that would be helpful! :)

Target Market(s)

Small and micro business owners

Industry/Entity Type

Marketing

Number of Pages Required

1 page

Font styles to use
Sans Serif
Other font styles liked:
• Montserrat

Colors
87cfc6
d2a4cc
ffffff
85cae6
e8e8e8
5c5c5c

Requirements
Must have
• Use of my brand colours: #cc8eb2, #76d6c8, #68c7ff as well as white and #595959. Must be visually pleasing / engaging, designed for desktop (as it's a desktop application), really easy to use / navigate.
• Use font Montserrat light & Montserrat Regular or Bold. Mostly should be Montserrat light.
Nice to have
• Would be nice to see how this would look on mobile (as the application is responsive) but this is not mandatory.
Should not have
• Should not look too corporate or dry.

```html
<!DOCTYPE html>
<html lang="en">
<head>
<meta charset="utf-8">
<title>Your Business – Who You Are</title>
<link href="https://fonts.googleapis.com/css2?family=Montserrat:wght@300;400;500;600;700&display=swap" rel="stylesheet">
<style>
  :root {
    --bar: #595959;
    --pink: #cc8eb2;
    --pink-tab: #d08fb8;
    --teal: #76d6c8;
    --sky: #68c7ff;
    --white: #ffffff;
    --panel: #f2f2f4;
    --field: #f7f7f9;
    --field-line: #d8d8de;
    --label: #555555;
    --hint: #b4b4bc;
    --tip: #4d4d4d;
  }
  * { box-sizing: border-box; margin: 0; padding: 0; }
  html, body {
    width: 1200px; height: 1200px; overflow: hidden;
    background: var(--white);
    font-family: "Montserrat", sans-serif;
    font-weight: 300;
  }
  .canvas { position: relative; width: 1200px; height: 1200px; }

  /* top bar */
  .topbar { position: absolute; left: 0; top: 0; width: 1200px; height: 37px; background: var(--bar); color: var(--white); }
  .brand { position: absolute; left: 162px; top: 10px; font-size: 16px; font-weight: 400; letter-spacing: 0.5px; display: flex; align-items: center; gap: 6px; }
  .brand-dot { width: 8px; height: 8px; border-radius: 50%; background: var(--teal); }
  .main-nav a { position: absolute; top: 11px; font-size: 13px; font-weight: 500; color: var(--white); text-decoration: none; }
  .main-nav .is-active { left: 353px; top: 6px; width: 66px; height: 24px; border: 1px solid var(--teal); border-radius: 12px; color: var(--teal); text-align: center; line-height: 22px; }
  .profile { position: absolute; left: 1032px; top: 10px; font-size: 14px; font-weight: 500; display: flex; align-items: center; gap: 7px; }

  /* step tabs */
  .steps { position: absolute; left: 154px; top: 61px; height: 40px; display: flex; }
  .step { height: 40px; background: var(--sky); color: var(--white); font-size: 13px; font-weight: 500; display: flex; align-items: center; justify-content: center; border-right: 1px solid rgba(255,255,255,0.35); }
  .step.is-current { background: var(--pink-tab); position: relative; }
  .step.is-current::after { content: ""; position: absolute; left: 58px; bottom: -7px; border: 7px solid transparent; border-bottom: 0; border-top-color: var(--pink-tab); }
  .step:last-child { border-right: 0; border-radius: 0 2px 2px 0; }

  /* panel */
  .panel { position: absolute; left: 154px; top: 129px; width: 968px; height: 1013px; background: var(--panel); }
  .section-title { position: absolute; left: 190px; top: 158px; font-size: 16px; font-weight: 700; color: var(--pink); letter-spacing: 0.3px; }
  .section-rule { position: absolute; left: 190px; top: 184px; width: 861px; height: 1px; background: var(--pink); opacity: 0.6; }

  .label { position: absolute; font-size: 13px; font-weight: 400; color: var(--label); display: flex; align-items: center; gap: 6px; }
  .help { width: 19px; height: 19px; border-radius: 50%; background: var(--teal); color: var(--white); font-size: 11px; font-weight: 500; display: inline-flex; align-items: center; justify-content: center; }

  .field { position: absolute; background: var(--field); border: 1px solid var(--field-line); border-radius: 3px; font-size: 11px; color: var(--hint); display: flex; align-items: center; padding-left: 13px; gap: 8px; }
  .area { position: absolute; background: var(--field); border: 1px solid var(--field-line); border-radius: 3px; }
  .grip { position: absolute; right: 3px; bottom: 3px; }

  /* tooltip */
  .tooltip { position: absolute; left: 277px; top: 258px; width: 310px; height: 26px; background: var(--tip); color: var(--white); font-size: 11px; font-weight: 400; border-radius: 3px; display: flex; align-items: center; justify-content: center; }
  .tooltip::after { content: ""; position: absolute; left: 35px; bottom: -5px; border: 5px solid transparent; border-bottom: 0; border-top-color: var(--tip); }

  /* colour picker */
  .chip { width: 23px; height: 23px; border-radius: 2px; background: #7f94c4; flex: none; }
  .picker { position: absolute; left: 642px; top: 354px; width: 211px; height: 222px; background: var(--white); box-shadow: 0 2px 6px rgba(0,0,0,0.08); }
  .swatches { position: absolute; left: 10px; top: 4px; display: grid; grid-template-columns: repeat(7, 24px); gap: 4px; }
  .swatches span { width: 24px; height: 24px; border-radius: 2px; }
  .current { position: absolute; left: 19px; top: 180px; width: 182px; display: flex; align-items: center; gap: 10px; font-size: 11px; font-weight: 400; color: var(--label); }
  .current-field { width: 128px; height: 32px; border: 1px solid #e4e4e8; border-radius: 2px; display: flex; align-items: center; gap: 8px; padding-left: 3px; color: var(--hint); font-size: 11px; }

  .save { position: absolute; left: 921px; top: 1068px; width: 132px; height: 39px; border-radius: 20px; background: var(--teal); color: var(--white); font-size: 13px; font-weight: 700; display: flex; align-items: center; justify-content: center; border: 0; font-family: inherit; }
</style>
</head>
<body>
<div class="canvas">

  <header class="topbar">
    <div class="brand"><span>BLOOMPATH</span><span class="brand-dot"></span></div>
    <nav class="main-nav">
      <a class="is-active">Plan</a>
      <a style="left:436px">Learn</a>
      <a style="left:504px">Remember</a>
    </nav>
    <div class="profile">My Profile
      <svg width="8" height="5" viewBox="0 0 8 5"><path d="M0 0h8L4 5z" fill="#fff"/></svg>
    </div>
  </header>

  <nav class="steps">
    <div class="step is-current" style="width:136px">Your Business</div>
    <div class="step" style="width:107px">Your Value</div>
    <div class="step" style="width:129px">Your Product</div>
    <div class="step" style="width:146px">Your Customers</div>
    <div class="step" style="width:111px">Your Goals</div>
    <div class="step" style="width:130px">Your Plan</div>
  </nav>

  <main class="panel"></main>

  <h2 class="section-title">WHO YOU ARE</h2>
  <div class="section-rule"></div>

  <!-- logo -->
  <div class="label" style="left:192px;top:208px">Upload your company Logo</div>
  <div class="field" style="left:190px;top:233px;width:411px;height:37px">
    <svg width="18" height="12" viewBox="0 0 18 12"><path d="M4.5 12A4 4 0 0 1 4 4 5 5 0 0 1 13.5 3.2 4.4 4.4 0 0 1 14 12z" fill="#b8b8c0"/><path d="M9 5l-2.5 2.6h1.6V10h1.8V7.6h1.6z" fill="#fff"/></svg>
    Upload Logo File, JPG or PNG
  </div>

  <!-- business name -->
  <div class="label" style="left:646px;top:208px">Business name</div>
  <div class="field" style="left:643px;top:233px;width:411px;height:37px">Type Your Business Name</div>

  <!-- tag line -->
  <div class="label" style="left:192px;top:290px">Business Tag Line <span class="help">?</span></div>
  <div class="field" style="left:190px;top:317px;width:411px;height:36px"></div>

  <!-- brand colours -->
  <div class="label" style="left:646px;top:292px">Brand colours</div>
  <div class="field" style="left:643px;top:317px;width:411px;height:36px;padding-left:9px"><span class="chip"></span>#C0C2CE</div>

  <!-- bio -->
  <div class="label" style="left:192px;top:374px">Business Bio <span class="help">?</span></div>
  <div class="area" style="left:190px;top:401px;width:411px;height:120px">
    <svg class="grip" width="8" height="8" viewBox="0 0 8 8" fill="#bbb"><circle cx="7" cy="1" r=".8"/><circle cx="4" cy="4" r=".8"/><circle cx="7" cy="4" r=".8"/><circle cx="1" cy="7" r=".8"/><circle cx="4" cy="7" r=".8"/><circle cx="7" cy="7" r=".8"/></svg>
  </div>
  <div class="area" style="left:643px;top:401px;width:411px;height:120px">
    <svg class="grip" width="8" height="8" viewBox="0 0 8 8" fill="#bbb"><circle cx="7" cy="1" r=".8"/><circle cx="4" cy="4" r=".8"/><circle cx="7" cy="4" r=".8"/><circle cx="1" cy="7" r=".8"/><circle cx="4" cy="7" r=".8"/><circle cx="7" cy="7" r=".8"/></svg>
  </div>

  <!-- competitors -->
  <div class="label" style="left:192px;top:541px">Key Competitors <span class="help">?</span></div>
  <div class="area" style="left:190px;top:568px;width:864px;height:120px">
    <svg class="grip" width="8" height="8" viewBox="0 0 8 8" fill="#bbb"><circle cx="7" cy="1" r=".8"/><circle cx="4" cy="4" r=".8"/><circle cx="7" cy="4" r=".8"/><circle cx="1" cy="7" r=".8"/><circle cx="4" cy="7" r=".8"/><circle cx="7" cy="7" r=".8"/></svg>
  </div>

  <!-- SWOT -->
  <div class="label" style="left:192px;top:709px">Strengths <span class="help">?</span></div>
  <div class="area" style="left:190px;top:735px;width:411px;height:120px">
    <svg class="grip" width="8" height="8" viewBox="0 0 8 8" fill="#bbb"><circle cx="7" cy="1" r=".8"/><circle cx="4" cy="4" r=".8"/><circle cx="7" cy="4" r=".8"/><circle cx="1" cy="7" r=".8"/><circle cx="4" cy="7" r=".8"/><circle cx="7" cy="7" r=".8"/></svg>
  </div>
  <div class="label" style="left:646px;top:709px">Weaknesses <span class="help">?</span></div>
  <div class="area" style="left:643px;top:735px;width:411px;height:120px">
    <svg class="grip" width="8" height="8" viewBox="0 0 8 8" fill="#bbb"><circle cx="7" cy="1" r=".8"/><circle cx="4" cy="4" r=".8"/><circle cx="7" cy="4" r=".8"/><circle cx="1" cy="7" r=".8"/><circle cx="4" cy="7" r=".8"/><circle cx="7" cy="7" r=".8"/></svg>
  </div>
  <div class="label" style="left:192px;top:876px">Opportunities <span class="help">?</span></div>
  <div class="area" style="left:190px;top:902px;width:411px;height:120px">
    <svg class="grip" width="8" height="8" viewBox="0 0 8 8" fill="#bbb"><circle cx="7" cy="1" r=".8"/><circle cx="4" cy="4" r=".8"/><circle cx="7" cy="4" r=".8"/><circle cx="1" cy="7" r=".8"/><circle cx="4" cy="7" r=".8"/><circle cx="7" cy="7" r=".8"/></svg>
  </div>
  <div class="label" style="left:646px;top:876px">Threats <span class="help">?</span></div>
  <div class="area" style="left:643px;top:902px;width:411px;height:120px">
    <svg class="grip" width="8" height="8" viewBox="0 0 8 8" fill="#bbb"><circle cx="7" cy="1" r=".8"/><circle cx="4" cy="4" r=".8"/><circle cx="7" cy="4" r=".8"/><circle cx="1" cy="7" r=".8"/><circle cx="4" cy="7" r=".8"/><circle cx="7" cy="7" r=".8"/></svg>
  </div>

  <!-- tooltip -->
  <div class="tooltip">Explain the value of your business in 5 words or less</div>

  <!-- colour picker -->
  <div class="picker">
    <div class="swatches">
      <span style="background:#e8524e"></span><span style="background:#ec7069"></span><span style="background:#f08c84"></span><span style="background:#eb9a4b"></span><span style="background:#eea96c"></span><span style="background:#f1b88a"></span><span style="background:#f3f3f3"></span>
      <span style="background:#ebb54a"></span><span style="background:#eec46a"></span><span style="background:#f0cf88"></span><span style="background:#e8cf4a"></span><span style="background:#eedb80"></span><span style="background:#f1de8a"></span><span style="background:#d4d4d4"></span>
      <span style="background:#e6e04a"></span><span style="background:#eae86a"></span><span style="background:#eeed8c"></span><span style="background:#afd64a"></span><span style="background:#c2e070"></span><span style="background:#cce58a"></span><span style="background:#a9a9a9"></span>
      <span style="background:#3dbd4a"></span><span style="background:#62cc6a"></span><span style="background:#80d484"></span><span style="background:#3aa5a5"></span><span style="background:#5fb6b8"></span><span style="background:#7cc4c4"></span><span style="background:#7a7a7a"></span>
      <span style="background:#4f74b8"></span><span style="background:#6e8bc2"></span><span style="background:#8ba3d0"></span><span style="background:#7558b8"></span><span style="background:#8b76c4"></span><span style="background:#9f90ce"></span><span style="background:#404040"></span>
      <span style="background:#9152b8"></span><span style="background:#a673c4"></span><span style="background:#b78ccf"></span><span style="background:#c94f92"></span><span style="background:#d571a8"></span><span style="background:#dd8cb6"></span><span style="background:#000000"></span>
    </div>
    <div class="current">Current
      <div class="current-field"><span class="chip"></span>#C0C2CE</div>
    </div>
  </div>

  <button class="save">Save Changes</button>
</div>
</body>
</html>
```